Our Chalet for rent needs a new website

Hi guys we have a chalet for rent and we finally want to have our own website for information and bookings the information is posted below and will upload pictures in due course.

Thanks

Chalet | 5 bedrooms | sleeps 11

Key Info
Beach or lakeside relaxationSkiGreat for children of all agesSome pets are welcome - please contact the ownerPrivate gardenCar advised
Exceptionally renovated Fern Byre dates from 1781 and offers the discerning skier a chance to stay in a wonderful mountain lodge. Spacious and light, there is a superb double aspect living and dining area and open-plan kitchen. All bedrooms are ensuite,and facilities include a sauna, enormous 6m 'Swim spa' hot tub, open-fireplace and separate treatment room on request. This chalet is perfect for families and groups!

Previously featured in Plate and Journey magazine and The Courier, chalet Fern Byre can be counted as one of only a handful of authentic farmhouses in the Chamonix valley available for rental. Located in the charming village of Les Houches, only minutes walk to the ski and mountain bike lifts, amenities, shops and several delightful restaurants and just a short drive from Chamonix town and the other ski/bike areas of the Chamonix valley.

The chalet is run as a luxury boutique hotel and is offered with total flexibility in mind. In winter the chalet provides luxury catered or self catered accommodation. In summer the chalet can be offered B&B or self catered. Our service can include in resort driving, airport transfers, and as experienced professionals with more than 27 yrs experience in Chamonix your holiday will be expertly delivered, whatever formula you choose!

Size Sleeps up to 11, 5 bedrooms
Nearest beach
Will consider Corporate bookings, House swap, Long term lets (over 1 month), Short breaks (1-4 days)
Access Car advised
Nearest Amenities 200 m
Nearest travel links Nearest airport: Geneva 100 km, Nearest railway: Les Houches 1 km
Family friendly Great for children of all ages, Suitable for people with restricted mobility
Notes Pets welcome, No smoking at this property
Features and Facilities

Luxuries Jacuzzi or hot tub, Sauna, Log fire, Internet access, DVD player
Pool Shared outdoor pool (unheated), Children's pool
General Central heating, TV, CD player, Table tennis, Safe, Satellite TV, Wi-Fi available
Standard Kettle, Toaster, Iron, Hair dryer
Utilities Clothes dryer, Dishwasher, Cooker, Microwave, Fridge, Freezer, Washing machine
Rooms 5 bedrooms, 5 bathrooms of which 5 En suites
Furniture Single beds (10), Cots (1), Dining seats for 12, Lounge seats for 12
Other High chair
Outdoors Shared outdoor pool (unheated), Balcony or terrace, Private garden, Shared garden, BBQ, Swing set
Access Parking
Further details indoors
With a myriad of chalets to choose from Chalet Fern Byre offers you something very special, the wonderful aimbience of a 230yr old Chamonix farmhouse married with modern, luxurious facilities. Owned and renovated by us over 5 years the Farm has been a labour of love..! but the attention to detail and quality of materials used has resulted in a very special property adored by all who stay.
Facilities include deep Italian leather sofa's juxtaposed with local mountain antiques and a modern granite and stainless steel kitchen married with hand-build cupboards. In the 5 bedrooms we have provided hotel standard zip-link beds so any room can be a double or a twin. We offer crisp, white, organic bed linen, goose feather duvets and leave you exclusive VOLA skincare bathroom products. The bathrooms are beautifully finished using Italian limestone tiles.
Wonderful valley views are framed from the huge picture windows, velux's and glass doors leading to the balcony. Our Eco features include geothermal generated underfloor heating, rain-water capture, clarivane double glazing, use of Dorvaplank, and re-use of the original wooden panels throughout providing a warm and indulgent ambience.
In the summer months we offer a private garden, ideal for al fresco dining plus the 'Swim-spa' hot tub provides a brilliant 'splash' pool for kids. We adorn the chalet with hanging baskets and can even offer a free minibus to Chamonix every morning for our B&B guests!
Chalet Fern Byre consists of the 2 upper floors of an ancient Alpine Farmhouse, with approximately 220 m2 of living space. The ground floor of the chalet is private (used by staff)
Further details outdoors
In Winter we provide bath-robes and crocs for the exterior 6m x 2.2m 'Swim Spa' hot tub, perfect for apres ski lounging!
In the summer months we offer a private side garden with BBQ, garden furniture, swings, table-tennis and the 'Swim-spa' hot tub provides a brilliant 'splash' pool for kids. We adorn the chalet with hanging baskets and the flower-covered balcony provides an ideal location for enjoying a cool drink and admiring the wonderful views.
Further details
Winter rentals are exclusive for groups. Rentals can be catered or self catered, for weeks or weekends, we are very flexible!
All Holidays can include our minibus service and airport transfers. Credit cards accepted.
Free concierge to book all ski packs, lessons or summer guides and mountain bikes.
Breakages deposit required for all rentals.
Summer holidays are self-catered or B&B.
Pressure washer available for mountian bikes.
The Rhone/French Alps region

The Mont Blanc massif offers an adrenalin packed holiday destination both winter and summer!

In winter you could ski 3 countries in one holiday! France, Switzerland and Italy! Boundless pistes and off piste variations including the famous 21km Combe Argentée trail (with a Guide)

In summer you can walk the 'Circuit des Crêtes Grises' and visit a host of charming villages and towns whilst admiring stunning Alpine pastures packed with the flora and fauna of the High Alps.

Locations worthy of a visit include Lake Annecy and the Old town of Annecy, the Pointe de Vorlan cable-car (Chamonix) for a wonderful view of the Alps and the Mont Blanc at 4807m (the highest mountain Peak in Europe). The Ice caves (accessed by the Belrioz railway) of the Combe Argentée are also worth a visit and for culture, Lyon, with its myriad of excellent shopping and restaurants and local exhibitions and museums.

Chamonix

Home to the sports of skiing and mountaineering, Chamonix is simply addictive. The dramatic mountains of the Chamonix valley incorporating the Mont Blanc Massif offers breathtaking scenery and make it a stunning setting for any skiing, snowboarding or summer activity holiday. With five separate ski areas scattered along the Chamonix valley, each with its own unique character and the famous off piste Combe Argentée run , every level of skier and snowboarder is amply catered for!

Les Houches is a pretty and unspoilt ski village which nestles just 5km from Chamonix town.

Les Houches is the largest single, pisted area in the Chamonix valley and has the added bonus of 86 snow canons covering 23 hectares of piste, this ski domain has wonderful skiing for beginners, intermediates and especially families.

The Chamonix valley has plenty to offer the non-skier, both rich in history and buzzing with shops, markets, bars, restaurants, exhibitions and festivals. There is also an seemingly unlimited variety of activities, from rock and ice climbing or snow shoe walking to x country and husky sledding. Chamonix is more than just a ski resort - it's a thriving mountain community, offering something for everyone. So join us this winter, you'll find our ski chalets simply gorgeous, our service attentive, our value for money excellent and your holiday experience simply unforgettable.

```html
<!DOCTYPE html>
<html lang="en">
<head>
<meta charset="utf-8">
<title>Fern Byre – Holiday Rental Chalet</title>
<link href="https://fonts.googleapis.com/css2?family=Alegreya:ital,wght@0,400;0,700;1,400&family=Roboto:ital,wght@0,300;0,400;0,700;1,300&display=swap" rel="stylesheet">
<style>
:root{
  --page-bg:#ececec;
  --dark:#1f1f1f;
  --gold:#b8965a;
  --gold-dark:#a98548;
  --text:#333;
  --muted:#555;
  --rule:#c9c9c9;
  --quote-bg:#efefef;
  --white:#fff;
}
*{box-sizing:border-box;margin:0;padding:0}
html,body{width:946px;height:1200px;overflow:hidden}
body{background:var(--page-bg);font-family:'Roboto',sans-serif;color:var(--text);position:relative}
.site{position:absolute;left:44px;top:0;width:858px;height:1200px;background:var(--white);box-shadow:0 0 6px rgba(0,0,0,.25)}
.inner{position:absolute;left:74px;width:710px}

/* top bar */
.topbar{position:absolute;top:0;left:0;width:100%;height:30px;background:var(--dark)}
.topbar .inner{top:0;height:30px;display:flex;justify-content:flex-end;align-items:center;gap:14px;font-family:'Alegreya',serif;font-size:9px;color:#eee}
.topbar .contact{display:flex;align-items:center;gap:5px}
.btn-book{background:var(--gold);color:#fff;font-weight:700;font-size:8.5px;padding:3px 11px;margin-left:2px}

/* header */
.header .inner{top:30px;height:84px}
.brand{position:absolute;left:0;top:16px}
.brand-name{font-family:'Alegreya',serif;font-size:27px;color:#333;line-height:1;padding-bottom:3px;border-bottom:1px solid #bbb;letter-spacing:.3px}
.brand-tag{font-family:'Alegreya',serif;font-style:italic;font-size:8.4px;color:#888;text-align:center;margin-top:4px;letter-spacing:.7px}
.nav{position:absolute;right:0;top:40px;display:flex;gap:26px;font-size:10px;font-weight:700;letter-spacing:.1px;color:#222}

/* hero */
.hero{position:absolute;top:114px;left:0;width:858px;height:406px;background:linear-gradient(100deg,#3a3020 0%,#9a6a2c 25%,#5a4330 45%,#2e3a78 62%,#3a4a8e 80%,#26306a 100%)}
.hero-snow{position:absolute;left:0;bottom:0;width:100%;height:120px;background:linear-gradient(180deg,rgba(170,170,230,0) 0%,rgba(190,190,235,.55) 100%)}
.hero-caption{position:absolute;left:503px;top:259px;width:281px;height:65px;background:rgba(30,30,30,.72);padding:10px 22px 0 0;text-align:right;font-family:'Alegreya',serif;font-weight:700;font-size:17px;line-height:22px;color:#fff}

/* booking */
.booking{position:absolute;left:118px;top:476px;width:710px;height:71px;background:var(--dark);padding:22px 23px 0}
.booking form{display:flex;gap:7px}
.field{width:129px;height:27px;background:#fff;display:flex;align-items:center;justify-content:space-between;padding:0 8px;font-size:10px;color:#aaa;font-weight:300}
.btn-check{width:119px;height:27px;background:var(--gold);color:#fff;font-family:'Alegreya',serif;font-weight:700;font-size:10.5px;display:flex;align-items:center;justify-content:center}

/* columns */
.col{position:absolute;top:588px;width:222px}
.col h2,.testimonials h2{font-family:'Alegreya',serif;font-weight:700;font-size:10.5px;letter-spacing:.2px;color:#222;padding-bottom:5px;border-bottom:1px solid var(--rule)}
.thumb{display:block;margin-top:15px;width:222px;height:130px}
.col p{margin-top:15px;font-size:8.6px;font-weight:300;line-height:14.8px;color:#333}
.features{list-style:none;margin-top:15px}
.features li{display:flex;align-items:center;gap:6px;font-size:8.6px;font-weight:300;height:18px;color:#333}
.more{position:absolute;top:276px;right:0;font-family:'Alegreya',serif;font-weight:700;font-size:8.4px;color:var(--gold);text-decoration:underline}

/* testimonials */
.testimonials{position:absolute;left:118px;top:915px;width:710px}
.testimonials h2{position:relative;border-bottom-color:#aaa}
.arrows{position:absolute;right:0;top:0;display:flex;gap:6px}
.quotes{display:flex;gap:21px;margin-top:15px}
.quote{width:344px}
.quote blockquote{position:relative;background:var(--quote-bg);height:85px;padding:13px 15px 0;font-size:8.3px;font-style:italic;font-weight:300;line-height:14.8px;color:#333}
.quote blockquote::after{content:"";position:absolute;left:16px;bottom:-13px;border-left:0 solid transparent;border-right:14px solid transparent;border-top:13px solid var(--quote-bg)}
.quote cite{display:block;margin-top:22px;font-style:normal;font-size:8.8px;font-weight:400;color:#222}

/* footer */
.footer{position:absolute;left:0;top:1110px;width:858px;height:90px;background:var(--dark);text-align:center}
.footer-nav{display:flex;justify-content:center;gap:18px;margin-top:26px;font-family:'Alegreya',serif;font-weight:700;font-size:8.6px;letter-spacing:.3px;color:#ccc}
.copyright{display:flex;justify-content:center;align-items:center;gap:8px;margin-top:12px;font-size:7.8px;color:#bbb}
.social{display:flex;gap:3px}
.social span{width:10px;height:10px;background:#aaa;display:block}
</style>
</head>
<body>
<div class="site">

  <div class="topbar">
    <div class="inner">
      <span class="contact">
        <svg width="9" height="10" viewBox="0 0 10 10"><path d="M2 0.5 L3.6 2.8 L2.6 4 Q3.8 6.4 6 7.4 L7.2 6.4 L9.5 8 L8.3 9.6 Q3.5 9 0.5 2 Z" fill="#eee"/></svg>
        +33 1 47 20 38 15
      </span>
      <span class="contact">
        <svg width="10" height="8" viewBox="0 0 10 8"><rect x="0" y="0" width="10" height="8" fill="#eee"/><path d="M0 0 L5 4.5 L10 0" fill="none" stroke="#1f1f1f" stroke-width="1"/></svg>
        info@FernByre.com
      </span>
      <span class="btn-book">Book NOW »</span>
    </div>
  </div>

  <header class="header">
    <div class="inner">
      <div class="brand">
        <div class="brand-name">Fern Byre</div>
        <div class="brand-tag">Holiday Rental Chalet</div>
      </div>
      <nav class="nav">
        <span>CHALET DETAILS</span><span>RATES</span><span>LOCATION</span><span>TESTIMONIALS</span><span>CONTACT US</span>
      </nav>
    </div>
  </header>

  <section class="hero" role="img" aria-label="Wooden mountain chalet lit warmly at dusk in deep snow, with snowy peaks under a blue evening sky">
    <div class="hero-snow"></div>
    <div class="hero-caption">The Wonderful Mountain Lodge<br>in the Chamonix Valley</div>
  </section>

  <div class="booking" style="left:74px">
    <form>
      <div class="field">Check In
        <svg width="9" height="9" viewBox="0 0 9 9"><rect x="0.5" y="0.5" width="8" height="8" fill="none" stroke="#444"/><path d="M0.5 2.5 H8.5 M2.5 4 V8 M4.5 4 V8 M6.5 4 V8 M0.5 5.2 H8.5 M0.5 6.8 H8.5" stroke="#444" stroke-width=".7"/></svg>
      </div>
      <div class="field">Check Out
        <svg width="9" height="9" viewBox="0 0 9 9"><rect x="0.5" y="0.5" width="8" height="8" fill="none" stroke="#444"/><path d="M0.5 2.5 H8.5 M2.5 4 V8 M4.5 4 V8 M6.5 4 V8 M0.5 5.2 H8.5 M0.5 6.8 H8.5" stroke="#444" stroke-width=".7"/></svg>
      </div>
      <div class="field">Adults
        <svg width="9" height="6" viewBox="0 0 9 6"><path d="M1 1 L4.5 4.5 L8 1" fill="none" stroke="#222" stroke-width="1.8"/></svg>
      </div>
      <div class="field">Children
        <svg width="9" height="6" viewBox="0 0 9 6"><path d="M1 1 L4.5 4.5 L8 1" fill="none" stroke="#222" stroke-width="1.8"/></svg>
      </div>
      <div class="btn-check">Check Availability »</div>
    </form>
  </div>

  <section class="col" style="left:74px">
    <h2>OVERVIEW</h2>
    <div class="thumb" role="img" aria-label="Warm living room with stone fireplace, wooden floor, rug and leather sofas" style="background:linear-gradient(135deg,#6a4a2a 0%,#b07a30 45%,#d8a24a 70%,#5a3a20 100%)"></div>
    <p>Lorem ipsum dolor sit amet, consectetur adipiscing elit. Phasellus eros lectus, iaculis a tincidunt in, vestib ulum non sapien. In hac habitasse platea dictumst. Nulla facilisi. In hac habitasse platea dictumst. Ut pellentesque, magna et faucibus faucibus justo velit. bibendum elit, sit amet commogo libero sem vitae.</p>
    <span class="more">Read More »</span>
  </section>

  <section class="col" style="left:318px">
    <h2>KEY FEATURES</h2>
    <div class="thumb" role="img" aria-label="Bedroom under timber beams with iron bed, white linen and window view" style="background:linear-gradient(135deg,#4a3a2a 0%,#7a6048 40%,#c8b8a0 65%,#3a2a1e 100%)"></div>
    <ul class="features">
      <li><svg width="11" height="9" viewBox="0 0 11 9"><path d="M1 4.5 L4 7.5 L10 1" fill="none" stroke="#b8965a" stroke-width="2"/></svg>5 bedrooms / Sleeps up to 11</li>
      <li><svg width="11" height="9" viewBox="0 0 11 9"><path d="M1 4.5 L4 7.5 L10 1" fill="none" stroke="#b8965a" stroke-width="2"/></svg>Family friendly / Great for children of all ages</li>
      <li><svg width="11" height="9" viewBox="0 0 11 9"><path d="M1 4.5 L4 7.5 L10 1" fill="none" stroke="#b8965a" stroke-width="2"/></svg>Pets welcome</li>
      <li><svg width="11" height="9" viewBox="0 0 11 9"><path d="M1 4.5 L4 7.5 L10 1" fill="none" stroke="#b8965a" stroke-width="2"/></svg>No smoking</li>
      <li><svg width="11" height="9" viewBox="0 0 11 9"><path d="M1 4.5 L4 7.5 L10 1" fill="none" stroke="#b8965a" stroke-width="2"/></svg>Internet Agccess</li>
    </ul>
    <span class="more">Learn More »</span>
  </section>

  <section class="col" style="left:561px">
    <h2>LOCATION / ACTIVITIES NEARBY</h2>
    <div class="thumb" role="img" aria-label="Street map of Les Houches showing the chalet's location" style="background:linear-gradient(135deg,#e6e3dc 0%,#dcd8ce 50%,#e8e4da 100%)"></div>
    <p>Proin velit elit, congue sed condimentum sed, vestib ulum vitae eros. Pellentesque blandit imperdiet ligula, at gravida nisl ultricies et. Sed rutrum consectetur neque. Morbi faucibus ipsum id dui sagittis adipiscng. Morbi id tincidunt massa, at suscipit urna ipsm dolor. sit amet, consectetur adipiscing elit donec a lectus in.</p>
    <span class="more">Learn More »</span>
  </section>

  <section class="testimonials" style="left:74px">
    <h2>TESTIMONIALS
      <span class="arrows">
        <svg width="6" height="9" viewBox="0 0 6 9"><path d="M5 1 L1.5 4.5 L5 8" fill="none" stroke="#999" stroke-width="1.6"/></svg>
        <svg width="6" height="9" viewBox="0 0 6 9"><path d="M1 1 L4.5 4.5 L1 8" fill="none" stroke="#999" stroke-width="1.6"/></svg>
      </span>
    </h2>
    <div class="quotes">
      <figure class="quote">
        <blockquote>Tom and Gina Harlow have built up a small portfolio of high-end properties run to exacting standards. Chalet Fern Byre is a sensitively restored farmhouse...with 24 years' experience operating chalets in the Chamonix area and a genuine passion for organic food and the environment..</blockquote>
        <cite>Plate and Journey Magazine January 2010</cite>
      </figure>
      <figure class="quote">
        <blockquote>Lorem ipsum dolor sit amet, consectetur adipiscing elit. Phasellus eros lectus, iaculis a tincidunt in, vestib ulum non sapien. In hac habitasse platea dictumst. Nulla facilisi. In hac habitasse platea dictumst. Ut pellentesque, magna et faucibus faucibus justo. velit. bibendum elit, sit amet commogo libero sem vitae os. Duis ultricies, risus vel.</blockquote>
        <cite>Martin Orlescu, Cypress, CA USA</cite>
      </figure>
    </div>
  </section>

  <footer class="footer">
    <nav class="footer-nav">
      <span>HOME</span><span>CHALET DETAILS</span><span>RATES</span><span>LOCATION</span><span>TESTIMONIALS</span><span>CONTACT US</span><span>BOOK NOW</span>
    </nav>
    <div class="copyright">
      <span>©2013 Fern Byre. All Rights Reserved.</span>
      <span class="social" aria-label="Social links"><span></span><span></span><span></span></span>
    </div>
  </footer>

</div>
</body>
</html>
```